Business cards for a recruitment company
Marrowby Associates
Modern
Helena Marrowby
Managing Director
PO Box 48213 Corvel Harbour Plaza Dubai United Arab Emirates
lena@marrowbyassociates-mail.test
marrowbyassociates-mail.test
The business card needs to have my name, designation etc in both English and Arabic. Therefore, both languages will appear on the front of the card. The final design will illustrate how two different translations will appear on the front of the card. **The logo must also appear on the front of the card.
The back of the card will be plain white with just the logo as attached in the AI file. Perhaps the logo could be indented.

```html
<!DOCTYPE html>
<html lang="en">
<head>
<meta charset="utf-8">
<title>Marrowby Associates – Business Cards</title>
<link rel="stylesheet" href="https://fonts.googleapis.com/css2?family=Montserrat:wght@400;600&family=Cairo:wght@400;600&display=swap">
<style>
  :root {
    --stage: #d9d9db;
    --card-white: #f7f7f8;
    --card-black: #1c1b1e;
    --ink: #1d1d1f;
    --purple: #8e6fa3;
    --purple-deep: #6f4f86;
    --grey-text: #555;
    --white: #ffffff;
  }
  * { box-sizing: border-box; margin: 0; padding: 0; }
  html, body { width: 1200px; height: 895px; overflow: hidden; }
  body {
    background: var(--stage);
    font-family: "Montserrat", Arial, sans-serif;
    color: var(--ink);
    position: relative;
  }
  .card {
    position: absolute;
    width: 540px;
    height: 309px;
    border-radius: 4px;
    overflow: hidden;
    box-shadow: 0 6px 18px rgba(0,0,0,.18);
  }

  /* ---------- back ---------- */
  .card--back {
    left: 610px;
    top: 80px;
    background: var(--card-black);
  }
  .web-tab {
    position: absolute;
    left: 0;
    top: 196px;
    height: 26px;
    padding: 0 18px 0 24px;
    background: var(--purple);
    border-radius: 0 13px 13px 0;
    color: var(--white);
    font-size: 12px;
    line-height: 26px;
    letter-spacing: .3px;
  }
  .wordmark {
    display: flex;
    align-items: center;
    gap: 12px;
    font-family: "Montserrat", Arial, sans-serif;
    font-weight: 400;
    text-transform: uppercase;
  }
  .wordmark__dot {
    border-radius: 50%;
    flex: none;
  }
  .wordmark__name { line-height: 1; }
  .wordmark__name span { display: block; }
  .card--back .wordmark {
    position: absolute;
    left: 200px;
    top: 108px;
    color: var(--white);
  }
  .card--back .wordmark__dot { width: 46px; height: 46px; background: var(--white); }
  .card--back .wordmark__name .line1 { font-size: 34px; letter-spacing: 1px; }
  .card--back .wordmark__name .line2 { font-size: 15px; letter-spacing: 6.5px; margin-top: 6px; }

  /* ---------- front ---------- */
  .card--front {
    left: 60px;
    top: 470px;
    background: var(--card-white);
  }
  .card--front .wordmark {
    position: absolute;
    left: 30px;
    top: 34px;
    color: var(--purple-deep);
  }
  .card--front .wordmark__dot { width: 34px; height: 34px; background: var(--purple-deep); }
  .card--front .wordmark__name .line1 { font-size: 25px; letter-spacing: .8px; }
  .card--front .wordmark__name .line2 { font-size: 11px; letter-spacing: 5px; margin-top: 5px; }

  .identity {
    position: absolute;
    left: 30px;
    top: 112px;
  }
  .identity__en, .identity__ar {
    display: flex;
    align-items: center;
    gap: 10px;
  }
  .identity__en { font-size: 15px; }
  .identity__name { font-weight: 600; letter-spacing: .5px; }
  .identity__title { color: var(--purple); font-size: 11px; letter-spacing: .6px; }
  .divider { width: 2px; height: 16px; background: var(--purple); }
  .identity__ar {
    margin-top: 6px;
    font-family: "Cairo", Arial, sans-serif;
    direction: rtl;
    justify-content: flex-end;
    font-size: 15px;
  }
  .identity__ar .identity__title { font-size: 13px; }

  .contacts {
    position: absolute;
    left: 30px;
    top: 182px;
    font-size: 12px;
    color: var(--grey-text);
    list-style: none;
  }
  .contacts__row { display: flex; align-items: center; gap: 22px; margin-bottom: 10px; }
  .contact { display: flex; align-items: center; gap: 7px; }
  .icon { width: 15px; height: 15px; flex: none; }

  .email-bar {
    position: absolute;
    left: 16px;
    right: 16px;
    bottom: 18px;
    height: 26px;
    border-radius: 13px;
    background: var(--card-black);
    color: var(--white);
    font-size: 12px;
    display: flex;
    align-items: center;
    justify-content: flex-end;
    gap: 8px;
    padding-right: 18px;
  }
</style>
</head>
<body>

  <section class="card card--back" aria-label="Card back">
    <div class="web-tab">www.marrowbyassociates-mail.test</div>
    <div class="wordmark">
      <span class="wordmark__dot"></span>
      <span class="wordmark__name"><span class="line1">Marrowby</span><span class="line2">Associates</span></span>
    </div>
  </section>

  <section class="card card--front" aria-label="Card front">
    <div class="wordmark">
      <span class="wordmark__dot"></span>
      <span class="wordmark__name"><span class="line1">Marrowby</span><span class="line2">Associates</span></span>
    </div>

    <div class="identity">
      <p class="identity__en">
        <span class="identity__name">HELENA MARROWBY</span>
        <span class="divider"></span>
        <span class="identity__title">MANAGING DIRECTOR</span>
      </p>
      <p class="identity__ar" lang="ar">
        <span class="identity__name">هيلينا ماروبي</span>
        <span class="divider"></span>
        <span class="identity__title">المدير العام</span>
      </p>
    </div>

    <ul class="contacts">
      <li class="contacts__row">
        <span class="contact">
          <svg class="icon" viewBox="0 0 16 16"><circle cx="8" cy="8" r="8" fill="#8e6fa3"/><path d="M8 3.5a3 3 0 0 0-3 3c0 2.2 3 5.5 3 5.5s3-3.3 3-5.5a3 3 0 0 0-3-3zm0 4.1a1.1 1.1 0 1 1 0-2.2 1.1 1.1 0 0 1 0 2.2z" fill="#fff"/></svg>
          PO Box 48213 Corvel Harbour Plaza
        </span>
      </li>
      <li class="contacts__row">
        <span class="contact">
          <svg class="icon" viewBox="0 0 16 16"><circle cx="8" cy="8" r="8" fill="#8e6fa3"/><path d="M5.3 4h1.6l.7 1.9-1 .7a5.6 5.6 0 0 0 2.8 2.8l.7-1 1.9.7v1.6c0 .5-.4.8-.9.8A6.9 6.9 0 0 1 4.5 4.9c0-.5.3-.9.8-.9z" fill="#fff"/></svg>
          020 418 5526
        </span>
        <span class="contact">
          <svg class="icon" viewBox="0 0 16 16"><circle cx="8" cy="8" r="8" fill="#8e6fa3"/><path d="M5.3 4h1.6l.7 1.9-1 .7a5.6 5.6 0 0 0 2.8 2.8l.7-1 1.9.7v1.6c0 .5-.4.8-.9.8A6.9 6.9 0 0 1 4.5 4.9c0-.5.3-.9.8-.9z" fill="#fff"/></svg>
          020 418 5526
        </span>
      </li>
    </ul>

    <div class="email-bar">
      <svg class="icon" viewBox="0 0 16 16"><circle cx="8" cy="8" r="8" fill="#8e6fa3"/><rect x="4" y="5" width="8" height="6" rx="1" fill="#fff"/><path d="M4.3 5.4 8 8.3l3.7-2.9" fill="none" stroke="#8e6fa3" stroke-width="1"/></svg>
      lena@marrowbyassociates-mail.test
    </div>
  </section>

</body>
</html>
```